Stationery Required - Own Logo provided

Hi,

We are a retail company called 'Copperfinch Trading Limited' based in the UK and would like some corporate stationery designed.

We have provided our Logo which we would like to use (Its attached to this brief)...

The designs must be orginal, professional, stylish and interesting!

Target Market(s)

We will use this stationery to communicate with our wholesale suppliers and employees, so it must have a 'professional' feel about it.

Industry/Entity Type

It Company

Requirements
Must have
• Must be professional, corporate, stylish and not to 'fussy'. we require ... Business card design, a4 letter, compliment slip. All designs must be supplied in a format where the text (address/telephone numbers etc..) can be edited, as we have alot of staff and operate out of several different premises.
Nice to have
• I would like a windows backround picture file supplied as well so we can integrate that onto our computer systems.

```html
<!DOCTYPE html>
<html lang="en">
<head>
<meta charset="utf-8">
<title>Copperfinch Trading Limited – Stationery Set</title>
<link href="https://fonts.googleapis.com/css2?family=Montserrat:wght@400;600;700&display=swap" rel="stylesheet">
<style>
  :root{
    --leaf:#95c11f;
    --forest:#3f5a23;
    --paper:#ffffff;
    --slip:#f4f4f4;
    --ink:#3d3d3d;
    --edge:#6b6b6b;
    --font:'Montserrat', Arial, sans-serif;
  }
  *{margin:0;padding:0;box-sizing:border-box}
  html,body{width:1200px;height:1200px;overflow:hidden;background:#fff}
  body{position:relative;font-family:var(--font);color:var(--ink)}
  .sheet{position:absolute;background:var(--paper);overflow:hidden}
  .sheet > svg.art{position:absolute;left:0;top:0;width:100%;height:100%}
  .sheet > *:not(svg){position:absolute}
  .brand{display:flex;align-items:center;gap:6px;color:var(--forest);font-weight:700;white-space:nowrap}
  .brand .mark{display:inline-block;background:var(--leaf)}
  .company-name{font-weight:700;color:#fff;white-space:nowrap}
  .contact{text-align:right;line-height:1.45;white-space:nowrap}
  .web{color:#fff;font-size:9px;white-space:nowrap}

  /* A4 letter */
  .letterhead{left:72px;top:96px;width:490px;height:694px;border:1px solid var(--edge)}
  .letterhead .brand{left:26px;top:42px;font-size:14px}
  .letterhead .brand .mark{width:13px;height:13px}
  .letterhead .company-name{right:14px;top:24px;font-size:10px}
  .letterhead .contact{right:14px;top:40px;font-size:5px;color:#fff}
  .letterhead .web{right:14px;bottom:7px;font-size:8.5px}

  /* business card */
  .card-front{left:671px;top:192px;width:211px;height:120px;border:1px solid var(--edge);border-radius:8px}
  .card-front .brand{left:20px;top:18px;font-size:8px;gap:4px}
  .card-front .brand .mark{width:8px;height:8px}
  .card-front .person{left:22px;top:40px;font-size:8.5px;font-weight:700;color:var(--forest)}
  .card-front .role{left:22px;top:53px;font-size:4.5px;line-height:1.9}
  .card-front .contact{right:12px;top:84px;font-size:4.5px;color:var(--ink)}
  .card-back{left:905px;top:192px;width:210px;height:118px;border-radius:8px}
  .card-back .brand{left:58px;top:44px;font-size:10px;color:#fff;gap:4px}
  .card-back .brand .mark{width:9px;height:9px;background:#fff}
  .card-back .web{right:12px;bottom:7px;font-size:4.5px}

  /* envelopes */
  .envelope-front{left:655px;top:436px;width:516px;height:340px;background:none;overflow:visible}
  .envelope-front .brand{left:26px;top:110px;font-size:17px}
  .envelope-front .brand .mark{width:15px;height:15px}
  .envelope-front .company-title{right:12px;top:106px;font-size:9.5px;font-weight:700;color:var(--forest)}
  .envelope-front .contact{right:12px;top:121px;font-size:5px}
  .envelope-front .web{right:14px;bottom:8px;font-size:9px}
  .envelope-back{left:655px;top:850px;width:516px;height:258px;background:none;overflow:visible}
  .envelope-back .flap-square{left:248px;top:28px;width:20px;height:20px;background:#fff}
  .envelope-front .flap-square{left:248px;top:30px;width:20px;height:20px;background:#fff}

  /* compliment slip */
  .compliment-slip{left:83px;top:886px;width:491px;height:209px;background:var(--slip);border:1px solid var(--edge)}
  .compliment-slip .brand{left:26px;top:30px;font-size:16px}
  .compliment-slip .brand .mark{width:15px;height:15px}
  .compliment-slip .greeting{left:247px;top:40px;font-size:17px;font-weight:700;color:var(--forest)}
  .compliment-slip .faint-square{left:200px;top:70px;width:70px;height:70px;background:#b7bfa6;opacity:.75}
  .compliment-slip .company-name{right:12px;top:132px;font-size:10px}
  .compliment-slip .contact{right:12px;top:148px;font-size:5px;color:#fff}
</style>
</head>
<body>

<section class="sheet letterhead" aria-label="A4 letterhead">
  <svg class="art" viewBox="0 0 490 694" preserveAspectRatio="none">
    <path d="M0,0 H490 V190 C440,84 300,2 0,4 Z" fill="var(--leaf)"/>
    <path d="M0,12 C300,10 440,92 490,204" fill="none" stroke="var(--forest)" stroke-width="6"/>
    <rect x="0" y="662" width="490" height="6" fill="var(--leaf)"/>
    <rect x="0" y="668" width="490" height="26" fill="var(--forest)"/>
  </svg>
  <div class="brand"><span class="mark"></span>Copperfinch Trading</div>
  <div class="company-name">Copperfinch Trading Limited</div>
  <div class="contact">Office address is 18 Mill Lane,<br>Ashbury, County Down BT30 4QX<br>Tel: 07700 900418<br>email hello@copperfinch.co.uk</div>
  <div class="web">www.copperfinch.co.uk</div>
</section>

<section class="sheet card-front" aria-label="Business card front">
  <svg class="art" viewBox="0 0 211 120" preserveAspectRatio="none">
    <path d="M0,110 C90,108 170,84 211,46 V120 H0 Z" fill="var(--leaf)"/>
    <path d="M0,106 C90,104 170,80 211,40" fill="none" stroke="var(--forest)" stroke-width="4"/>
  </svg>
  <div class="brand"><span class="mark"></span>Copperfinch</div>
  <div class="person">Owen Hartley</div>
  <div class="role">Company Director<br>07700 900418<br>Email hello@copperfinch.co.uk</div>
  <div class="contact">Office with<br>18 Mill Lane,<br>Ashbury, County Down BT30 4QX</div>
</section>

<section class="sheet card-back" aria-label="Business card back">
  <svg class="art" viewBox="0 0 210 118" preserveAspectRatio="none">
    <rect width="210" height="118" fill="var(--forest)"/>
    <path d="M0,0 H210 V34 C150,64 70,84 0,86 Z" fill="var(--leaf)"/>
    <path d="M0,88 C70,86 150,66 210,36" fill="none" stroke="#fff" stroke-width="2.5"/>
  </svg>
  <div class="brand"><span class="mark"></span>Copperfinch</div>
  <div class="web">www.copperfinch.co.uk</div>
</section>

<section class="sheet envelope-front" aria-label="Envelope front">
  <svg class="art" viewBox="0 0 516 340" preserveAspectRatio="none">
    <path d="M2,82 C2,60 10,50 40,42 L230,4 Q258,-2 286,4 L476,42 C506,50 514,60 514,82 Z" fill="var(--leaf)"/>
    <rect x="0.5" y="80.5" width="515" height="259" fill="#fff" stroke="var(--edge)"/>
    <path d="M1,326 C200,320 400,250 515,168 V339 H1 Z" fill="var(--leaf)"/>
    <path d="M1,318 C200,312 400,240 515,158" fill="none" stroke="var(--forest)" stroke-width="6"/>
  </svg>
  <div class="flap-square"></div>
  <div class="brand"><span class="mark"></span>Copperfinch Trading</div>
  <div class="company-title">Copperfinch Trading Limited</div>
  <div class="contact">Office address is 18 Mill Lane,<br>Ashbury, County Down BT30 4QX<br>Tel: 07700 900418<br>email hello@copperfinch.co.uk</div>
  <div class="web">www.copperfinch.co.uk</div>
</section>

<section class="sheet envelope-back" aria-label="Envelope back">
  <svg class="art" viewBox="0 0 516 258" preserveAspectRatio="none">
    <rect x="0.5" y="0.5" width="515" height="257" fill="#fff" stroke="var(--edge)"/>
    <path d="M1,1 H515 V10 C515,24 505,30 480,36 L290,80 Q258,86 226,80 L36,36 C11,30 1,24 1,10 Z" fill="var(--leaf)"/>
  </svg>
  <div class="flap-square"></div>
</section>

<section class="sheet compliment-slip" aria-label="Compliment slip">
  <svg class="art" viewBox="0 0 491 209" preserveAspectRatio="none">
    <path d="M0,196 C200,190 380,120 491,42 V209 H0 Z" fill="var(--leaf)"/>
    <path d="M0,189 C200,183 380,112 491,34" fill="none" stroke="#fff" stroke-width="3"/>
    <path d="M0,194 C200,188 380,118 491,40" fill="none" stroke="var(--forest)" stroke-width="5"/>
  </svg>
  <div class="brand"><span class="mark"></span>Copperfinch Trading</div>
  <div class="greeting">With Compliments</div>
  <div class="faint-square"></div>
  <div class="company-name">Copperfinch Trading Limited</div>
  <div class="contact">Office address is 18 Mill Lane,<br>Ashbury, County Down BT30 4QX<br>Tel: 07700 900418<br>email hello@copperfinch.co.uk</div>
</section>

</body>
</html>
```